Finch Haulage Ltd

We need an A5 size (UK size) flyer to advertise our new business which is called Finch Haulage.
Domestic and Commercial Waste Clearance Services.
Please have the question in bold "Do you have a pile of junk you need to dispose of?"
We collect all kinds of junk or rubbish from homes and businesses across Kent, Sussex and South London.
No fuss, no mess!
A low cost, hassle free alternative to skip hire.
Licensed by the Landcare Board and fully insured (this can be in small print at the bottom).
Please put the Recycle symbol somewhere.
Our tagline on our vehicle is "We Clear More, For Less!"
We'd like the flyer to be bold and eye-catching (to catch the eye of the homeowner or business owner while it's sitting on their doormat).
We need our telephone, website and email to be prominent. Maybe saying "Call today for a free quote"
Tel. 01734 586019
Email: info@finchhaulage.example.co.uk
www.finchhaulage.example.co.uk
Target Market(s)
Our market will be homes and small businesses around Kent, Sussex and South London.

```html
<!DOCTYPE html>
<html lang="en">
<head>
<meta charset="utf-8">
<title>Finch Haulage – Waste Clearance Flyer</title>
<link rel="stylesheet" href="https://fonts.googleapis.com/css2?family=Oswald:wght@600;700&family=Montserrat:wght@600;700;800&family=Lato:wght@400&family=Fredoka:wght@600&display=swap">
<style>
  :root {
    --ink-dark: #2a2a2c;
    --ink-darker: #1f1f21;
    --green: #2fb457;
    --green-light: #4fd072;
    --green-deep: #1f9a44;
    --recycle-green: #5cc534;
    --recycle-shade: #3a9a22;
    --yellow: #f3d64a;
    --white: #ffffff;
    --paper: #f1f1f1;
    --text-grey: #3a3a3a;
    --phone-grey: #3b3b3b;
  }
  * { margin: 0; padding: 0; box-sizing: border-box; }
  html, body { width: 894px; height: 1200px; overflow: hidden; background: #d9d9d9; }

  .flyer {
    position: relative;
    width: 894px;
    height: 1200px;
    overflow: hidden;
    background: radial-gradient(ellipse at 40% 35%, #38383b 0%, var(--ink-dark) 55%, var(--ink-darker) 100%);
    font-family: "Montserrat", Arial, sans-serif;
  }

  .brand {
    position: absolute;
    left: 90px;
    top: 110px;
    font-weight: 800;
    font-size: 44px;
    letter-spacing: 2px;
    color: var(--white);
  }

  .headline-band {
    position: absolute;
    left: 0;
    top: 228px;
    width: 570px;
    height: 205px;
    background: linear-gradient(180deg, var(--green-light) 0%, var(--green) 60%, var(--green-deep) 100%);
    border-top: 6px solid var(--white);
    border-bottom: 6px solid var(--white);
  }
  .headline {
    position: absolute;
    left: 34px;
    top: 22px;
    font-family: "Oswald", "Arial Narrow", sans-serif;
    font-weight: 700;
    font-size: 46px;
    line-height: 53px;
    color: var(--white);
    text-transform: uppercase;
    letter-spacing: 0.5px;
  }
  .headline .accent { color: var(--yellow); }

  .photo-tile {
    position: absolute;
    border: 7px solid var(--white);
    border-radius: 34px;
    transform: rotate(45deg);
    box-shadow: 0 4px 14px rgba(0,0,0,0.45);
  }
  .photo-bike { left: 648px; top: 100px; width: 190px; height: 190px; background: linear-gradient(135deg, #8a8f96, #5e5a52); }
  .photo-mall { left: 462px; top: 268px; width: 150px; height: 150px; background: linear-gradient(135deg, #b9c1cb, #6c7480); }
  .photo-sofa { left: 636px; top: 276px; width: 222px; height: 222px; background: linear-gradient(135deg, #a8593e, #3a4a6a); }

  .tagline {
    position: absolute;
    left: 40px;
    top: 456px;
    font-weight: 700;
    font-size: 31px;
    color: var(--yellow);
    letter-spacing: 0.5px;
  }
  .intro {
    position: absolute;
    left: 40px;
    top: 514px;
    width: 840px;
    font-weight: 600;
    font-size: 15.5px;
    line-height: 24px;
    color: var(--white);
  }

  .lower-panel { position: absolute; left: 0; top: 0; }

  .recycle-mark {
    position: absolute;
    left: 640px;
    top: 618px;
    width: 170px;
    height: 170px;
  }

  .phone-block {
    position: absolute;
    left: 50px;
    top: 752px;
    width: 48px;
  }
  .phone-icon {
    width: 32px;
    height: 32px;
    margin-left: 6px;
    border-radius: 7px;
    background: var(--green);
  }
  .phone-number {
    position: absolute;
    left: -2px;
    top: 44px;
    font-family: "Oswald", "Arial Narrow", sans-serif;
    font-weight: 700;
    font-size: 42px;
    line-height: 48px;
    color: var(--phone-grey);
    white-space: nowrap;
    writing-mode: vertical-rl;
    letter-spacing: 1px;
  }

  .credentials {
    position: absolute;
    left: 218px;
    top: 748px;
    width: 600px;
    font-family: "Lato", Arial, sans-serif;
    font-weight: 400;
    font-size: 16px;
    line-height: 26.5px;
    color: var(--text-grey);
  }

  .footer {
    position: absolute;
    left: 0;
    top: 1098px;
    width: 894px;
    height: 102px;
    background: linear-gradient(180deg, var(--green-light) 0%, var(--green) 55%, var(--green-deep) 100%);
    color: var(--white);
  }
  .contact-row {
    position: absolute;
    left: 40px;
    right: 30px;
    top: 14px;
    display: flex;
    align-items: center;
    gap: 18px;
    font-weight: 700;
    font-size: 19px;
    white-space: nowrap;
  }
  .contact-row svg { flex: none; }
  .contact-item { display: flex; align-items: center; gap: 8px; }
  .small-print {
    position: absolute;
    left: 40px;
    top: 58px;
    font-weight: 600;
    font-size: 15.5px;
  }
</style>
</head>
<body>
<div class="flyer">

  <div class="brand">FINCH HAULAGE</div>

  <div class="photo-tile photo-bike" role="img" aria-label="Photo of an old rusty bicycle against a wall"></div>

  <div class="headline-band">
    <h1 class="headline">
      Do you have a pile<br>
      <span class="accent">of junk you need</span><br>
      to dispose of?
    </h1>
  </div>

  <div class="photo-tile photo-mall" role="img" aria-label="Photo of a busy shopping centre interior"></div>
  <div class="photo-tile photo-sofa" role="img" aria-label="Photo of old furniture and a television dumped against a brick wall"></div>

  <h2 class="tagline">WE CLEAR MORE, FOR LESS!</h2>
  <p class="intro">
    We offer affordable rubbish and junk clearance services<br>
    across Kent, Sussex and South London. Our friendly man &amp; van<br>
    teams provide a professional and reliable service to homes and businesses across the<br>
    region. We collect all kinds of unwanted junk and rubbish no matter how big or small,<br>
    from a single armchair to a full house, office or shop clearance at very<br>
    competitive rates.
  </p>

  <svg class="lower-panel" width="894" height="1200" viewBox="0 0 894 1200">
    <path d="M0,702 Q 650,640 838,1100 L0,1100 Z" fill="var(--green)"/>
    <path d="M0,718 Q 632,660 818,1100 L0,1100 Z" fill="var(--paper)"/>
    <defs>
      <path id="quote-curve" d="M292,688 Q 660,720 800,1010"/>
    </defs>
    <text font-family="Fredoka, Arial Rounded MT Bold, sans-serif" font-weight="600" font-size="42" fill="var(--yellow)" letter-spacing="1">
      <textPath href="#quote-curve">Call today for a free quote</textPath>
    </text>
  </svg>

  <svg class="recycle-mark" viewBox="0 0 180 180" role="img" aria-label="Recycle symbol">
    <defs>
      <marker id="recycle-head" viewBox="0 0 10 10" refX="3" refY="5" markerWidth="2.6" markerHeight="2.6" orient="auto">
        <path d="M0,0 L10,5 L0,10 Z" fill="var(--recycle-green)"/>
      </marker>
      <g id="recycle-arrow">
        <line x1="98" y1="40" x2="132" y2="99" stroke="var(--recycle-shade)" stroke-width="24" stroke-linecap="butt" transform="translate(2,3)"/>
        <line x1="98" y1="40" x2="132" y2="99" stroke="var(--recycle-green)" stroke-width="22" stroke-linecap="butt" marker-end="url(#recycle-head)"/>
      </g>
    </defs>
    <use href="#recycle-arrow"/>
    <use href="#recycle-arrow" transform="rotate(120 90 95)"/>
    <use href="#recycle-arrow" transform="rotate(240 90 95)"/>
  </svg>

  <div class="phone-block">
    <div class="phone-icon">
      <svg width="32" height="32" viewBox="0 0 32 32" aria-hidden="true">
        <path d="M10 8c1-1 2-1 3 0l2 3c.6 1 .3 2-.5 2.6l-1.2.9c.8 2 2.3 3.6 4.3 4.5l.9-1.2c.6-.8 1.7-1.1 2.6-.5l3 2c1 .7 1 1.9 0 2.8l-1.3 1.3c-1.3 1.3-3.4 1.4-5.5.3-3.6-1.9-6.4-4.7-8.300-8.3C8.9 13.3 9 11.2 10 9.9z" fill="var(--white)"/>
      </svg>
    </div>
    <div class="phone-number">01734 586019</div>
  </div>

  <p class="credentials">
    We are licensed by<br>
    the Landcare Board and fully<br>
    insured to dispose of your waste responsibly<br>
    and safely, in compliance with current legislation.<br>
    We are committed to diverting as much waste from<br>
    landfill as possible and we will always separate and recycle.<br>
    Any reusable items of furniture are donated to charity. From time<br>
    to time we can offer a load of rubble or soil free of charge to our<br>
    customers and would only charge for delivery, as part of our<br>
    commitment to reuse and recycle whenever possible. For every collection we<br>
    issue our clients with a waste transfer certificate so you can be assured that<br>
    your waste is being disposed of responsibly.
  </p>

  <footer class="footer">
    <div class="contact-row">
      <span class="contact-item">
        <svg width="24" height="17" viewBox="0 0 26 18" aria-hidden="true">
          <rect x="1" y="1" width="24" height="16" rx="1.5" fill="var(--white)"/>
          <path d="M2 2 L13 10 L24 2" fill="none" stroke="var(--green)" stroke-width="2"/>
        </svg>
        info@finchhaulage.example.co.uk
      </span>
      <span class="contact-item">
        <svg width="20" height="20" viewBox="0 0 22 22" aria-hidden="true">
          <g fill="none" stroke="var(--white)" stroke-width="1.8">
            <circle cx="11" cy="11" r="9.5"/>
            <ellipse cx="11" cy="11" rx="4.5" ry="9.5"/>
            <line x1="1.5" y1="11" x2="20.5" y2="11"/>
            <line x1="3" y1="6" x2="19" y2="6"/>
            <line x1="3" y1="16" x2="19" y2="16"/>
          </g>
        </svg>
        www.finchhaulage.example.co.uk
      </span>
    </div>
    <p class="small-print">Licensed by the Landcare Board and fully insured</p>
  </footer>

</div>
</body>
</html>
```